Stationary for Halcyon Elite Las Vegas
Business cards & letter head, etc
Stationary for Halcyon Elite Las Vegas - Hospitality Industry
Creative Brief
Use same font as used in my logo
Just make it look nice & professional
Professional
Miles Grant
Co-Founder and Managing Partner
We don't want an address listed
miles.t.grant@mailbox-demo.net
www.halcyonelitelasvegas-demo.com
We also need a second card with all of the same info except for the following changes: Name: Derek Malone Phone #: 555.014.7392 Email: Derek.Malonevip@mailbox-demo.net
Just use the logo

```html
<!DOCTYPE html>
<html lang="en">
<head>
<meta charset="utf-8">
<title>Halcyon Elite Las Vegas – Stationery</title>
<link rel="stylesheet" href="https://fonts.googleapis.com/css2?family=Montserrat:wght@400;600;700&display=swap">
<style>
  :root {
    --board: #c9c9ca;
    --paper: #ffffff;
    --ink: #2b2b2b;
    --muted: #7a7a7a;
    --brand: #1f9fd6;
    --brand-soft: #dbeef8;
    --card: #0c0c0c;
    --card-text: #e6e6e6;
    --rule: #9a9a9a;
  }
  * { box-sizing: border-box; margin: 0; padding: 0; }
  html, body { width: 1200px; height: 679px; overflow: hidden; }
  body {
    background: var(--board);
    font-family: "Montserrat", Arial, sans-serif;
    color: var(--ink);
    position: relative;
  }
  .label {
    position: absolute;
    font-size: 8px;
    font-weight: 600;
    color: #333;
    text-align: center;
    white-space: nowrap;
  }
  .label.card-label { font-size: 6.5px; width: 124px; }
  .sheet {
    position: absolute;
    background: var(--paper);
    box-shadow: 0 1px 3px rgba(0,0,0,.25);
  }
  .brand-name {
    font-family: "Montserrat", Arial, sans-serif;
    font-weight: 700;
    color: var(--brand);
    text-align: center;
    letter-spacing: .5px;
    line-height: 1.1;
    white-space: nowrap;
  }
  .page { top: 151px; width: 360px; height: 502px; }
  .page .brand-name { position: absolute; top: 22px; left: 0; right: 0; font-size: 15px; }
  .fax { left: 24px; }
  .letterhead { left: 403px; }
  .watermark {
    position: absolute;
    left: 40px; top: 200px; width: 200px; height: 210px;
    border-radius: 60% 40% 70% 30%;
    background: radial-gradient(ellipse at 40% 40%, var(--brand-soft), rgba(219,238,248,0) 70%);
  }
  .fax-code { position: absolute; right: 22px; top: 74px; font-size: 8px; font-weight: 700; }
  .fax-table {
    position: absolute; left: 17px; top: 90px; width: 325px;
    border-collapse: collapse; font-size: 6px;
  }
  .fax-table td { border: 1px solid var(--rule); height: 20px; padding: 0 4px; }
  .fax-table td.key { width: 38px; background: #f2f2f2; }
  .fax-table td.val { width: 124px; }
  .fax-options {
    position: absolute; left: 17px; top: 182px; width: 325px;
    display: flex; justify-content: space-between; font-size: 6px;
  }
  .fax-options span { display: flex; align-items: center; gap: 3px; }
  .fax-options i { display: inline-block; width: 7px; height: 7px; border: 1px solid var(--rule); }
  .page-footer {
    position: absolute; left: 17px; right: 17px; bottom: 12px;
    border-top: 1px solid var(--brand);
    padding-top: 4px;
    display: flex; gap: 14px; align-items: center;
    font-size: 5px; color: var(--muted);
  }
  .page-footer .accent { width: 18px; height: 3px; background: var(--brand); margin-top: -9px; align-self: flex-start; }
  .page-footer span { display: flex; align-items: center; gap: 2px; }

  .card {
    position: absolute; top: 34px; width: 112px; height: 64px;
    background: var(--card); border-radius: 6px;
    box-shadow: 0 1px 3px rgba(0,0,0,.35);
    color: var(--card-text);
  }
  .card .brand-name { position: absolute; top: 11px; left: 0; right: 0; font-size: 6.5px; letter-spacing: .2px; }
  .card-details {
    position: absolute; left: 0; right: 0; top: 25px;
    text-align: center; font-size: 4.6px; line-height: 1.4; white-space: nowrap;
  }
  .card-details strong { color: var(--brand); font-weight: 600; font-size: 5.6px; }
  .card.back .brand-name { top: 26px; font-size: 8px; }

  .envelope { left: 782px; width: 394px; }
  .envelope.front { top: 163px; height: 185px; }
  .envelope.front .brand-name { position: absolute; left: 16px; top: 16px; font-size: 12px; text-align: left; }
  .envelope.back { top: 379px; height: 173px; }
  .envelope.back svg { position: absolute; inset: 0; }
</style>
</head>
<body>
  <div class="label" style="left:24px;top:139px;width:360px;">Fax Cover</div>
  <div class="label" style="left:403px;top:139px;width:360px;">Letterhead</div>
  <div class="label card-label" style="left:772px;top:22px;">Business Card (Miles Grant)</div>
  <div class="label card-label" style="left:892px;top:22px;">Business Card (Derek Malone)</div>
  <div class="label card-label" style="left:1012px;top:22px;">Business Card (Back)</div>
  <div class="label" style="left:782px;top:151px;width:394px;">Envelope (Front)</div>
  <div class="label" style="left:782px;top:367px;width:394px;">Envelope (Back)</div>

  <section class="sheet page fax">
    <div class="brand-name">Halcyon Elite Las Vegas</div>
    <div class="fax-code">XXX</div>
    <table class="fax-table">
      <tr><td class="key">To:</td><td class="val"></td><td class="key">From:</td><td class="val"></td></tr>
      <tr><td class="key">Fax:</td><td class="val"></td><td class="key">Pages:</td><td class="val"></td></tr>
      <tr><td class="key">Phone:</td><td class="val"></td><td class="key">Date:</td><td class="val"></td></tr>
      <tr><td class="key">Re:</td><td class="val"></td><td class="key">CC:</td><td class="val"></td></tr>
    </table>
    <div class="fax-options">
      <span><i></i>Urgent</span><span><i></i>For Review</span><span><i></i>Please Comment</span><span><i></i>Please Reply</span><span><i></i>Please Recycle</span>
    </div>
    <div class="watermark" style="top:210px;" role="img" aria-label="Faint feather-like decorative motif"></div>
    <footer class="page-footer">
      <div class="accent"></div>
      <span><svg width="5" height="5" viewBox="0 0 10 10"><path d="M2 1l2 2-1 1.5c.6 1.2 1.3 1.9 2.5 2.5L7 6l2 2-1.5 1.5C4.5 9 1 5.5.5 2.5z" fill="#1f9fd6"/></svg>555.014.7392</span>
      <span>miles.t.grant@mailbox-demo.net</span>
      <span>www.halcyonelitelasvegas-demo.com</span>
    </footer>
  </section>

  <section class="sheet page letterhead">
    <div class="brand-name">Halcyon Elite Las Vegas</div>
    <div class="watermark" role="img" aria-label="Faint feather-like decorative motif"></div>
    <footer class="page-footer">
      <div class="accent"></div>
      <span><svg width="5" height="5" viewBox="0 0 10 10"><path d="M2 1l2 2-1 1.5c.6 1.2 1.3 1.9 2.5 2.5L7 6l2 2-1.5 1.5C4.5 9 1 5.5.5 2.5z" fill="#1f9fd6"/></svg>555.014.7392</span>
      <span>miles.t.grant@mailbox-demo.net</span>
      <span>www.halcyonelitelasvegas-demo.com</span>
    </footer>
  </section>

  <article class="card" style="left:778px;">
    <div class="brand-name">Halcyon Elite Las Vegas</div>
    <div class="card-details">
      <strong>Miles Grant</strong><br>Co-Founder and Managing Partner<br>555.014.7392<br>miles.t.grant@mailbox-demo.net<br>www.halcyonelitelasvegas-demo.com
    </div>
  </article>
  <article class="card" style="left:898px;">
    <div class="brand-name">Halcyon Elite Las Vegas</div>
    <div class="card-details">
      <strong>Derek Malone</strong><br>Co-Founder and Managing Partner<br>555.014.7392<br>Derek.Malonevip@mailbox-demo.net<br>www.halcyonelitelasvegas-demo.com
    </div>
  </article>
  <article class="card back" style="left:1018px;">
    <div class="brand-name">Halcyon Elite Las Vegas</div>
  </article>

  <section class="sheet envelope front">
    <div class="brand-name">Halcyon Elite Las Vegas</div>
  </section>
  <section class="sheet envelope back">
    <svg viewBox="0 0 394 173" width="394" height="173">
      <path d="M0 0 L180 88 Q197 96 214 88 L394 0" fill="none" stroke="#1f9fd6" stroke-width="1.5"/>
      <path d="M0 0 L180 84 Q197 92 214 84 L394 0 Z" fill="#f7f7f7"/>
    </svg>
  </section>
</body>
</html>
```